Oven Cleaning Business owner needs business card design

Hi there,
Would like for a business card to be designed for myself, the owner of a professional oven cleaning business on the Sunshine Coast.
Would like it to look sleek, and modern-ish. Bit creative is encouraged too.
Include following:
Name/title: Corin ter Haghe, Owner
Phone number: 1300 482 916
Email: info@hearthshinecrew.com.au
Website: www.hearthshinecrew.com.au

```html
<!DOCTYPE html>
<html lang="en">
<head>
<meta charset="utf-8">
<title>Hearthshine Crew – Business Card</title>
<link href="https://fonts.googleapis.com/css2?family=Mulish:wght@500;700;800&display=swap" rel="stylesheet">
<style>
  :root {
    --teal: #52c4cb;
    --ink: #111314;
    --paper: #ffffff;
    --backdrop: #ecebe9;
  }
  * { margin: 0; padding: 0; box-sizing: border-box; }
  html, body { width: 1200px; height: 1200px; overflow: hidden; }
  body {
    position: relative;
    background: var(--backdrop);
    font-family: "Mulish", Arial, sans-serif;
    color: var(--ink);
  }
  .card {
    position: absolute;
    left: 298px;
    width: 605px;
    height: 346px;
    background: var(--paper);
    overflow: hidden;
  }
  .card--back { top: 208px; }
  .card--front { top: 674px; background: var(--teal); }

  /* contact side */
  .divider {
    position: absolute;
    width: 2px;
    background: var(--teal);
  }
  .divider--upper { left: 246px; top: 0; height: 192px; }
  .divider--lower { left: 263px; top: 149px; height: 197px; }

  .brand {
    position: absolute;
    display: flex;
    align-items: center;
    font-weight: 800;
    white-space: nowrap;
  }
  .brand__dot {
    flex: none;
    border-radius: 50%;
    background: var(--teal);
  }
  .card--back .brand {
    left: 22px; top: 82px;
    width: 212px;
    flex-direction: column;
    gap: 18px;
    font-size: 22px;
    color: var(--teal);
  }
  .card--back .brand__dot { width: 110px; height: 110px; }

  .contact-row {
    position: absolute;
    left: 287px;
    display: flex;
    align-items: center;
    gap: 14px;
    font-size: 18px;
    font-weight: 500;
  }
  .icon {
    flex: none;
    width: 30px; height: 30px;
    border-radius: 50%;
    background: var(--teal);
    display: flex; align-items: center; justify-content: center;
  }
  .icon svg { width: 18px; height: 18px; }
  .contact-row--name { top: 41px; align-items: flex-start; }
  .contact-row--name .name {
    font-size: 23px; font-weight: 700; line-height: 30px;
  }
  .contact-row--phone { top: 153px; }
  .contact-row--email { top: 212px; }
  .contact-row--web { top: 271px; }

  /* logo side */
  .front-panel {
    position: absolute;
    inset: 0;
    background: var(--paper);
    border-radius: 150px 90px 80px 210px / 110px 120px 90px 160px;
  }
  .card--front .brand {
    left: 0; right: 0; top: 116px;
    justify-content: center;
    gap: 20px;
    font-size: 36px;
    color: var(--ink);
  }
  .card--front .brand__dot { width: 104px; height: 104px; }
</style>
</head>
<body>
  <section class="card card--back">
    <span class="divider divider--upper"></span>
    <span class="divider divider--lower"></span>

    <div class="brand">
      <span class="brand__dot"></span>
      <span class="brand__name">Hearthshine Crew</span>
    </div>

    <div class="contact-row contact-row--name">
      <span class="icon">
        <svg viewBox="0 0 24 24" fill="#fff"><circle cx="12" cy="8" r="4.5"/><path d="M3.5 21c0-4.7 3.8-7.5 8.5-7.5s8.5 2.8 8.5 7.5z"/></svg>
      </span>
      <p class="name">Corin ter Haghe,<br>Owner</p>
    </div>

    <div class="contact-row contact-row--phone">
      <span class="icon">
        <svg viewBox="0 0 24 24" fill="#fff"><path d="M6.6 10.8c1.4 2.8 3.8 5.1 6.6 6.6l2.2-2.2c.3-.3.7-.4 1-.2 1.1.4 2.3.6 3.6.6.6 0 1 .4 1 1V20c0 .6-.4 1-1 1C10.6 21 3 13.4 3 4c0-.6.4-1 1-1h3.5c.6 0 1 .4 1 1 0 1.3.2 2.5.6 3.6.1.3 0 .7-.2 1z"/></svg>
      </span>
      <span>1300 482 916</span>
    </div>

    <div class="contact-row contact-row--email">
      <span class="icon">
        <svg viewBox="0 0 24 24" fill="none" stroke="#fff" stroke-width="2"><rect x="3" y="5.5" width="18" height="13" rx="1"/><path d="M3.5 6.5 12 13l8.5-6.5"/></svg>
      </span>
      <span>info@hearthshinecrew.com.au</span>
    </div>

    <div class="contact-row contact-row--web">
      <span class="icon">
        <svg viewBox="0 0 24 24" fill="none" stroke="#fff" stroke-width="1.8"><circle cx="12" cy="12" r="9"/><ellipse cx="12" cy="12" rx="4" ry="9"/><path d="M3 12h18M4.5 7.5h15M4.5 16.5h15"/></svg>
      </span>
      <span>www.hearthshinecrew.com.au</span>
    </div>
  </section>

  <section class="card card--front">
    <div class="front-panel"></div>
    <div class="brand">
      <span class="brand__dot"></span>
      <span class="brand__name">Hearthshine Crew</span>
    </div>
  </section>
</body>
</html>
```